Electrician's Business needs web site for customers to get professional impression of business.

Have a logo, need a web page for customers to visit. Web page should make it easy for customers to approach /contact me, if possible a way for customers to leave their details so I can call them back.
A description/ list of services and advertise how my service is different and better than other electricians.
A gallery to upload photos to, to show completed works from past projects.
Updates

Target Market(s)

Domestic/residential home owner/renter/builder

Industry/Entity Type

Electrician

Coding

Coded - Design and coding required

Number of Pages Required

2 page

Font styles to use
Sans Serif

Colors
0255a3
ffffff

Requirements
Must have
• Appeal to home owner/renter, domestic market.
• Capture contact details of customer & advertise my contact details.
• List of services
Nice to have
• A photo gallery, so I can upload pictures of completed work.
Should not have
• Industrial/construction images.

```html
<!DOCTYPE html>
<html lang="en">
<head>
<meta charset="utf-8">
<title>Voltline Electrical Services</title>
<link href="https://fonts.googleapis.com/css2?family=Roboto:wght@300;400;500;700&display=swap" rel="stylesheet">
<style>
:root{
  --blue:#0255a3;
  --blue-dark:#0e4a93;
  --blue-deep:#0b3f80;
  --orange:#f07f1e;
  --white:#ffffff;
  --ink:#1d1d1d;
  --grey:#7a7a7a;
  --line:#e3e3e3;
  --mist:#e8eef6;
}
*{box-sizing:border-box;margin:0;padding:0}
html,body{width:1200px;height:3066px;overflow:hidden}
body{font-family:"Roboto",Arial,sans-serif;color:var(--ink);background:var(--white)}
.wrap{width:1000px;margin:0 auto;position:relative}

/* header */
.site-header{height:116px;background:var(--blue-dark)}
.site-header .wrap{display:flex;align-items:center;height:116px;justify-content:space-between}
.brand{display:flex;align-items:center;gap:12px;color:var(--white);font-size:34px;font-weight:700}
.brand-dot{width:16px;height:16px;background:var(--orange)}
.nav{display:flex;gap:34px;align-items:center}
.nav a{color:var(--white);text-decoration:none;font-size:15px;font-weight:500;padding:8px 0;position:relative}
.nav a.active{color:var(--orange)}
.nav a.active::after{content:"";position:absolute;left:0;right:0;bottom:-8px;height:2px;background:var(--orange)}

/* hero */
.hero{height:548px;position:relative;background:linear-gradient(120deg,#6f7a6d 0%,#8c8a7c 35%,#b7b4ad 65%,#d9d9d6 100%);display:flex;align-items:center;justify-content:center;text-align:center;color:var(--white)}
.hero-inner{margin-top:-20px}
.hero h1{font-size:48px;font-weight:700;letter-spacing:.5px;text-shadow:0 2px 6px rgba(0,0,0,.35)}
.hero p{width:860px;margin:8px auto 28px;font-size:15px;line-height:24px}
.btn-solid{display:inline-block;background:var(--blue);color:var(--white);font-size:19px;font-weight:500;padding:15px 44px;text-decoration:none}
.hero-arrow{position:absolute;top:362px;width:54px;height:54px;border:2px solid rgba(255,255,255,.8);border-radius:50%;display:flex;align-items:center;justify-content:center;background:rgba(0,0,0,.15)}
.hero-arrow.prev{left:24px}.hero-arrow.next{right:24px}

/* section titles */
.section-title{font-size:30px;font-weight:700;text-align:center;color:var(--ink)}
.section-title span{color:var(--blue)}

/* welcome */
.welcome{height:542px;padding-top:45px}
.welcome .lead{width:820px;margin:22px auto 0;text-align:center;font-size:14px;line-height:24px;color:var(--grey)}
.services{display:flex;justify-content:space-between;margin-top:106px}
.service-card{width:307px;height:250px;border:1px solid var(--line);text-align:center;position:relative;padding-top:72px}
.service-icon{position:absolute;top:-62px;left:50%;margin-left:-62px;width:124px;height:124px;border-radius:50%;background:var(--blue);border:6px solid var(--white);box-shadow:0 0 0 2px var(--line);display:flex;align-items:center;justify-content:center}
.service-card h3{font-size:19px;font-weight:500;margin-bottom:16px}
.service-card p{font-size:12px;line-height:22px;color:var(--grey);padding:0 22px}
.more{display:inline-flex;align-items:center;gap:6px;margin-top:22px;color:var(--orange);font-size:12px;font-weight:500;text-decoration:none}

/* projects */
.projects{height:434px;background:var(--mist);padding-top:34px}
.projects .pager{position:absolute;right:0;top:8px;display:flex;gap:4px}
.pager span{width:20px;height:20px;background:#9aa2ac;display:flex;align-items:center;justify-content:center}
.project-grid{display:flex;justify-content:space-between;margin-top:33px}
.project-card{width:242px;background:var(--white);box-shadow:0 12px 14px -8px rgba(0,0,0,.25)}
.photo{display:block}
.project-card .photo{height:164px}
.project-card .body{padding:18px 18px 18px;height:106px}
.project-card h4{font-size:15px;font-weight:500;color:var(--orange);margin-bottom:8px}
.project-card p{font-size:12px;line-height:18px;color:var(--grey)}

/* about */
.about{height:470px;background:linear-gradient(90deg,var(--blue-deep),var(--blue));color:var(--white);padding-top:40px}
.about .section-title{color:var(--white)}
.about-row{display:flex;justify-content:space-between;margin-top:40px}
.about-text{width:470px}
.about-text h3{font-size:19px;font-weight:500;margin-bottom:20px}
.about-text p{font-size:13px;line-height:24px;color:#d6e2f1;margin-bottom:16px}
.btn-line{display:inline-block;margin-top:28px;border:1px solid var(--white);color:var(--white);text-decoration:none;padding:12px 24px;font-size:17px}
.about-photo{width:482px;height:300px;border:6px solid #5b8cc6;margin-top:-16px;background:linear-gradient(135deg,#c9cfd6,#7b7f8a 45%,#37435c)}

/* gallery */
.gallery{height:623px;padding-top:42px}
.gallery-grid{display:grid;grid-template-columns:repeat(4,242px);justify-content:space-between;row-gap:9px;margin-top:38px}
.gallery-grid .photo{height:217px}

/* footer */
.site-footer{height:265px;background:var(--blue-dark);color:var(--white);padding-top:38px}
.footer-cols{position:relative;height:220px}
.fcol{position:absolute;top:0}
.fcol h5{font-size:13px;font-weight:700;margin-bottom:18px;letter-spacing:.3px}
.fcol li{list-style:none;font-size:11px;line-height:27px;color:#dbe5f2}
.fcol p{font-size:11px;line-height:18px;color:#dbe5f2}
.news-input{width:240px;height:40px;background:var(--white);margin-top:22px;font-size:11px;color:#999;padding:13px 12px}
.news-btn{display:inline-block;margin-top:16px;background:var(--orange);color:var(--white);font-size:11px;padding:12px 10px}
.contact li{display:flex;gap:8px;align-items:center}
.bottom-bar{height:68px;background:var(--blue-deep);color:#dbe5f2;font-size:11px}
.bottom-bar .wrap{display:flex;justify-content:space-between;align-items:center;height:68px}
.social{display:flex;align-items:center;gap:16px}
.social i{width:11px;height:11px;border-radius:50%;background:#dbe5f2;display:inline-block}
</style>
</head>
<body>

<header class="site-header">
  <div class="wrap">
    <div class="brand"><span class="brand-dot"></span>Voltline</div>
    <nav class="nav">
      <a class="active" href="#">HOME</a>
      <a href="#">SERVICES</a>
      <a href="#">ABOUT US</a>
      <a href="#">PROJECTS</a>
      <a href="#">GALLERY</a>
      <a href="#">CONTACT US</a>
      <svg width="16" height="16" viewBox="0 0 16 16"><circle cx="6.5" cy="6.5" r="5" fill="none" stroke="#fff" stroke-width="2"/><line x1="10" y1="10" x2="15" y2="15" stroke="#fff" stroke-width="2"/></svg>
    </nav>
  </div>
</header>

<section class="hero" role="img" aria-label="Electrician in hard hat working on a home electrical meter">
  <div class="hero-inner">
    <h1>FAST AND RELIABLE ELECTRICAL SERVICES</h1>
    <p>Lorem ipsum dolor sit amet, consectetur adipiscing elit, sed do eiusmod tempor incididunt ut labore et dolore magna aliqua. Ut enim ad minim veniam, quis nostrud exercitation ullamco laboris nisi ut aliquip ex ea commodo consequat.</p>
    <a class="btn-solid" href="#">LEARN MORE</a>
  </div>
  <span class="hero-arrow prev"><svg width="14" height="14" viewBox="0 0 14 14"><path d="M9 2 4 7l5 5" fill="none" stroke="#fff" stroke-width="2"/></svg></span>
  <span class="hero-arrow next"><svg width="14" height="14" viewBox="0 0 14 14"><path d="M5 2l5 5-5 5" fill="none" stroke="#fff" stroke-width="2"/></svg></span>
</section>

<section class="welcome">
  <div class="wrap">
    <h2 class="section-title">WELCOME TO <span>VOLTLINE</span></h2>
    <p class="lead">Lorem ipsum dolor sit amet, cons ectetur elit. Vestibulum nec odios Suspe ndisse cursus mal suada faci lisis. Lorem ipsum dolor sit ametion consectetur elit. Vesti bulum nec odio ipsum.</p>
    <div class="services">
      <div class="service-card">
        <div class="service-icon"><svg width="50" height="54" viewBox="0 0 50 54"><circle cx="25" cy="20" r="15" fill="none" stroke="#fff" stroke-width="3"/><rect x="18" y="36" width="14" height="5" fill="#fff"/><rect x="19" y="43" width="12" height="4" fill="#fff"/><path d="M21 26l4-8 4 8" fill="none" stroke="#fff" stroke-width="2"/></svg></div>
        <h3>DIAGNOSIS AND REPAIRS</h3>
        <p>Sed ut perspiciatis unde omnis iste natus error sit voluptatem accusantium doloremque laudantium, totam rem aperiam, eaque ipsa quae.</p>
        <a class="more" href="#">READ MORE <svg width="11" height="11" viewBox="0 0 11 11"><circle cx="5.5" cy="5.5" r="5.5" fill="#f07f1e"/><path d="M4 3l2.5 2.5L4 8" fill="none" stroke="#fff" stroke-width="1.5"/></svg></a>
      </div>
      <div class="service-card">
        <div class="service-icon"><svg width="52" height="52" viewBox="0 0 52 52"><path d="M10 42 30 22" stroke="#fff" stroke-width="7" stroke-linecap="round"/><circle cx="34" cy="18" r="9" fill="none" stroke="#fff" stroke-width="5"/><path d="M14 12 40 40" stroke="#fff" stroke-width="4" stroke-linecap="round"/></svg></div>
        <h3>INSTALL AND UPGRADES</h3>
        <p>Sed ut perspiciatis unde omnis iste natus error sit voluptatem accusantium doloremque laudantium, totam rem aperiam, eaque ipsa quae.</p>
        <a class="more" href="#">READ MORE <svg width="11" height="11" viewBox="0 0 11 11"><circle cx="5.5" cy="5.5" r="5.5" fill="#f07f1e"/><path d="M4 3l2.5 2.5L4 8" fill="none" stroke="#fff" stroke-width="1.5"/></svg></a>
      </div>
      <div class="service-card">
        <div class="service-icon"><svg width="54" height="54" viewBox="0 0 54 54"><circle cx="27" cy="27" r="16" fill="none" stroke="#fff" stroke-width="6" stroke-dasharray="7 5"/><circle cx="27" cy="27" r="11" fill="none" stroke="#fff" stroke-width="3"/><circle cx="27" cy="27" r="4" fill="#fff"/></svg></div>
        <h3>ELECTRICAL MAINTENANCE</h3>
        <p>Sed ut perspiciatis unde omnis iste natus error sit voluptatem accusantium doloremque laudantium, totam rem aperiam, eaque ipsa quae.</p>
        <a class="more" href="#">READ MORE <svg width="11" height="11" viewBox="0 0 11 11"><circle cx="5.5" cy="5.5" r="5.5" fill="#f07f1e"/><path d="M4 3l2.5 2.5L4 8" fill="none" stroke="#fff" stroke-width="1.5"/></svg></a>
      </div>
    </div>
  </div>
</section>

<section class="projects">
  <div class="wrap">
    <h2 class="section-title">PAST <span>PROJECTS</span></h2>
    <div class="pager">
      <span><svg width="8" height="8" viewBox="0 0 8 8"><path d="M6 0 2 4l4 4" fill="none" stroke="#fff" stroke-width="1.5"/></svg></span>
      <span><svg width="8" height="8" viewBox="0 0 8 8"><path d="M2 0l4 4-4 4" fill="none" stroke="#fff" stroke-width="1.5"/></svg></span>
    </div>
    <div class="project-grid">
      <div class="project-card"><div class="photo" role="img" aria-label="Electrician in hard hat checking wiring" style="background:linear-gradient(135deg,#d9c48a,#8c7a5a 50%,#4c5a78)"></div><div class="body"><h4>EGESTAS AENEAN</h4><p>Sed ut perspiciatis unde omnis iste natus error sit voluptatem.</p></div></div>
      <div class="project-card"><div class="photo" role="img" aria-label="Technician working at an electrical panel" style="background:linear-gradient(135deg,#9aa6b6,#4d5f7c 55%,#2e3c56)"></div><div class="body"><h4>MATTIS IPSUM</h4><p>Sed ut perspiciatis unde omnis iste natus error sit voluptatem.</p></div></div>
      <div class="project-card"><div class="photo" role="img" aria-label="Electrician wiring a timber-framed room" style="background:linear-gradient(135deg,#c8a57a,#8a6a48 55%,#54606e)"></div><div class="body"><h4>TORTOR CONSECTETUR</h4><p>Sed ut perspiciatis unde omnis iste natus error sit voluptatem.</p></div></div>
      <div class="project-card"><div class="photo" role="img" aria-label="Two technicians servicing an outdoor air conditioning unit" style="background:linear-gradient(135deg,#c9d3de,#8b97a6 55%,#4e5d72)"></div><div class="body"><h4>DAPIBUS ADIPISCING</h4><p>Sed ut perspiciatis unde omnis iste natus error sit voluptatem.</p></div></div>
    </div>
  </div>
</section>

<section class="about">
  <div class="wrap">
    <h2 class="section-title">ABOUT US</h2>
    <div class="about-row">
      <div class="about-text">
        <h3>VOLTLINE</h3>
        <p>Sed ut perspiciatis unde omnis iste natus error sit voluptatem accusantium doloremque laudantium, totam rem aperiam, eaque ipsa quae ab illo inventore veritatis et quasi architecto beatae vitae dicta sunt explicabo.</p>
        <p>At vero eos et accusamus et iusto odio dignissimos ducimus qui blanditiis praesentium voluptatum deleniti atque corrupti quos dolores et quas molestias excepturi sint occaecati cupiditate non provident, similique sunt in culpa qui officia deserunt mollitia animi, id est laborum et dolorum fuga.</p>
        <a class="btn-line" href="#">READ MORE</a>
      </div>
      <div class="about-photo" role="img" aria-label="Electrician's tool belt with tools and a yellow hard hat"></div>
    </div>
  </div>
</section>

<section class="gallery">
  <div class="wrap">
    <h2 class="section-title">OUR <span>GALLERY</span></h2>
    <div class="gallery-grid">
      <div class="photo" role="img" aria-label="Electrician in blue overalls pulling on work gloves" style="background:linear-gradient(135deg,#dfe4ea,#5b7fb8 60%,#28487c)"></div>
      <div class="photo" role="img" aria-label="Smiling electrician beside an outdoor unit" style="background:linear-gradient(135deg,#b8c0ca,#5d6b80 55%,#2c3548)"></div>
      <div class="photo" role="img" aria-label="Electricians inspecting wiring in a switchboard" style="background:linear-gradient(135deg,#5a4a3a,#a26b3c 50%,#2f2a2a)"></div>
      <div class="photo" role="img" aria-label="Electrician in hard hat at a distribution board" style="background:linear-gradient(135deg,#c6ccd4,#4f6488 55%,#26344e)"></div>
      <div class="photo" role="img" aria-label="Multimeter testing a circuit breaker panel" style="background:linear-gradient(135deg,#c9b28f,#7a6a58 55%,#3a3a40)"></div>
      <div class="photo" role="img" aria-label="Electrician working inside a server cabinet" style="background:linear-gradient(135deg,#2a4e8a,#1a3664 55%,#0c1c36)"></div>
      <div class="photo" role="img" aria-label="Close view of hands connecting coloured wires" style="background:linear-gradient(135deg,#d8dde3,#6d8fb0 50%,#b5482e)"></div>
      <div class="photo" role="img" aria-label="Hands holding a screwdriver at an electrical outlet" style="background:linear-gradient(135deg,#e6ebf2,#6f96cf 55%,#2b5ba4)"></div>
    </div>
  </div>
</section>

<footer class="site-footer">
  <div class="wrap footer-cols">
    <div class="fcol" style="left:0">
      <h5>WELCOME</h5>
      <ul><li>Home</li><li>About Us</li><li>Services</li><li>Our Team</li><li>Clients</li><li>Blog</li></ul>
    </div>
    <div class="fcol" style="left:154px;width:250px">
      <h5>JOIN OUR NEWSLETTER</h5>
      <p>Excepteur sint occaecat cupidatat non proident, sunt in culpa qui</p>
      <div class="news-input">Enter Your Email</div>
      <span class="news-btn">SUBSCRIBE</span>
    </div>
    <div class="fcol" style="left:490px">
      <h5>INFORMATION</h5>
      <ul><li>Terms &amp; Conditions</li><li>Privacy policy</li><li>Disclaimer</li><li>Contact us</li><li>Sitemap</li></ul>
    </div>
    <div class="fcol" style="left:687px">
      <h5>WHY US</h5>
      <ul><li>Customers</li><li>Team</li><li>FAQ</li><li>News</li><li>Others</li></ul>
    </div>
    <div class="fcol contact" style="left:854px;width:160px">
      <h5>CONTACT INFO</h5>
      <ul>
        <li>Voltline</li>
        <li style="line-height:16px">NO, Street Name,<br>City Name, Country</li>
        <li><svg width="11" height="11" viewBox="0 0 11 11"><path d="M2 1h2l1 3-1.5 1a6 6 0 0 0 2.5 2.5L7 6l3 1v2a1 1 0 0 1-1 1A8 8 0 0 1 1 2a1 1 0 0 1 1-1z" fill="#dbe5f2"/></svg>+00 (0) 123 456 78</li>
        <li><svg width="12" height="9" viewBox="0 0 12 9"><rect width="12" height="9" fill="#dbe5f2"/><path d="M0 0l6 5 6-5" fill="none" stroke="#0e4a93" stroke-width="1"/></svg>hello@voltline-example.com</li>
      </ul>
    </div>
  </div>
</footer>
<div class="bottom-bar">
  <div class="wrap">
    <span>© 2016. Voltline. All rights reserved</span>
    <span class="social">Connect with our social network <i></i><i></i><i></i><i></i><i></i></span>
  </div>
</div>

</body>
</html>
```